New Website for ReBranded Company - CrewBeacon

We have a successful company and website currently but it is a little dated. We have re-branded the company from Harbor Signal Networks to CrewBeacon and have a new logo for the new name. We are looking to build a newer fresher website with the new name. I will need a concept of the home page and one inside page. You can see our current site at https://www.harborsignalnetworks.example and the new site will be https://www.crewbeacon.example .

I also really like the https://www.pathlantern.example/ website. I like ledgerkite.example website. I like the https://skillorbit.example/ website.

See the attached document for layout and some text to use. Use the pictures I attached as opposed to pictures from the old site as much as you can.

Target Market(s)

Business

Industry/Entity Type

Software Service

Number of Pages Required

2 page

Font styles to use
Sans Serif

Requirements
Must have
• Use the colors from my logo. Professional but modern. We want people to feel like our product makes their staff feel safer at work.
Should not have
• Don't use any red or orange (no stop colors).

```html
<!DOCTYPE html>
<html lang="en">
<head>
<meta charset="utf-8">
<title>CrewBeacon — Get Help Fast</title>
<link rel="stylesheet" href="https://fonts.googleapis.com/css2?family=Raleway:wght@300;400;500;600;700;800&family=Lato:wght@400;700&display=swap">
<style>
:root{
  --blue:#2f9ad8;
  --blue-dark:#1f7fc0;
  --green:#77bb34;
  --green-dark:#4f8a1e;
  --teal:#2fd0d8;
  --ink:#1b1b1b;
  --text:#555;
  --muted:#777;
  --dark-band:#2a2a2a;
  --footer-bg:#f5f5f5;
  --white:#fff;
}
*{box-sizing:border-box;margin:0;padding:0}
html,body{width:1200px;height:3441px;overflow:hidden}
body{position:relative;background:var(--white);font-family:'Raleway',sans-serif;color:var(--text)}
.abs{position:absolute}
.center{left:0;width:1200px;text-align:center}
.btn{display:inline-block;background:var(--blue);color:var(--white);font-family:'Lato',sans-serif;font-weight:700;font-size:11px;letter-spacing:.3px;padding:11px 18px;text-transform:uppercase;text-decoration:none}
.btn.white{background:var(--white);color:var(--ink)}

/* header */
.site-header{top:0;left:0;width:1200px;height:63px;background:var(--white)}
.brand{display:flex;align-items:center;gap:8px;font-family:'Raleway',sans-serif;font-weight:700;font-size:20px;color:var(--blue)}
.brand .dot{width:26px;height:26px;border-radius:50%;background:var(--blue)}
.site-header .brand{position:absolute;left:94px;top:17px}
.nav{position:absolute;right:94px;top:15px;display:flex;gap:10px;align-items:center;font-family:'Lato',sans-serif;font-size:11px;text-transform:uppercase}
.nav a{color:#333;text-decoration:none;padding:10px 12px}
.nav a.login{background:var(--blue);color:#fff;padding:10px 14px}
.nav a.explore{background:var(--green);color:#fff;padding:10px 14px}

/* hero */
.hero{top:63px;left:0;width:1200px;height:454px;background:linear-gradient(180deg,#3a3a38 0%,#55524c 45%,#3d4a3a 100%)}
.hero .shade{position:absolute;inset:0;background:rgba(0,0,0,.25)}
.hero-pre{top:188px;font-size:25px;font-weight:300;color:#fff;letter-spacing:.5px}
.hero-title{top:206px;font-size:58px;font-weight:800;color:#fff;letter-spacing:-.5px}
.hero-title em{font-style:normal;color:var(--green)}
.hero-sub{top:266px;font-size:23px;font-weight:400;color:#fff}
.hero-cta{top:313px}
.slide-arrow{top:255px;width:38px;height:26px;background:rgba(255,255,255,.25);display:flex;align-items:center;justify-content:center}
.slide-arrow.prev{left:0;border-radius:0 13px 13px 0}
.slide-arrow.next{right:0;border-radius:13px 0 0 13px}

/* feature cards */
.feature-card{top:506px;width:330px;height:250px}
.feature-card .photo{height:170px}
.feature-card .caption{height:80px;display:flex;align-items:center;justify-content:center;text-align:center;color:#fff;font-size:13.5px;line-height:1.4;padding:0 30px}
.feature-card.blue .caption{background:var(--blue)}
.feature-card.green .caption{background:var(--green)}

/* blue band */
.alone-band{top:816px;left:0;width:1200px;height:304px;background:linear-gradient(180deg,var(--blue) 0%,var(--teal) 100%)}
.alone-pre{top:888px;font-size:19px;font-weight:400;color:#fff}
.alone-title{top:912px;font-size:42px;font-weight:800;color:#fff}
.alone-sub{top:969px;font-size:14.5px;font-weight:400;color:#fff}
.alone-cta{top:1008px}

/* why */
.why-pre{top:1174px;font-size:18px;color:var(--ink)}
.why-title{top:1192px;font-size:42px;font-weight:800;color:var(--ink)}
.reason{top:1258px;width:336px;text-align:center}
.reason .icon{width:96px;height:108px;margin:0 auto;border-radius:10px 10px 48px 48px;background:linear-gradient(180deg,#e3f1fb,#bfe0f5);border:4px solid var(--blue)}
.reason h3{margin-top:22px;font-size:18px;font-weight:500;color:var(--ink);letter-spacing:.2px}
.reason p{margin-top:14px;font-family:'Lato',sans-serif;font-size:12px;line-height:1.55;color:var(--muted);padding:0 30px}
.reason .lead{font-family:'Lato',sans-serif;font-size:13px;color:#333;margin-top:12px;padding:0 0 8px;border-bottom:1px solid #ddd;margin-left:60px;margin-right:50px}
.options{display:grid;grid-template-columns:90px 70px;margin:8px 0 0 90px;text-align:left;font-family:'Lato',sans-serif;font-size:11px;color:#333;row-gap:6px}
.why-cta{top:1555px}

/* splits */
.photo-phone{left:94px;top:1645px;width:506px;height:326px;background:linear-gradient(135deg,#b9c2c4 0%,#6b6b68 50%,#3a3026 100%)}
.photo-lanyard{left:600px;top:1976px;width:506px;height:326px;background:linear-gradient(135deg,#cfd8da 0%,#1e2630 30%,#111822 70%,#b8c1c4 100%)}
.split-text{font-size:22px;font-weight:400;color:var(--ink);line-height:1.3;text-align:center}
.split-one{left:600px;top:1753px;width:506px}
.split-one-cta{left:600px;width:506px;top:1827px;text-align:center}
.split-two{left:94px;top:2090px;width:506px}
.split-two-note{left:94px;top:2167px;width:506px;text-align:center;font-family:'Lato',sans-serif;font-size:12px;color:#333}
.split-two-note small{font-size:9px;color:var(--muted)}

/* plan */
.plan-title{top:2370px;font-size:42px;font-weight:800;color:var(--ink)}
.plan-card{top:2449px;width:327px;height:266px;border-radius:28px;background:#fff;box-shadow:0 3px 12px rgba(0,0,0,.12);overflow:hidden;padding:16px 25px}
.plan-card.active{background:var(--green)}
.plan-card .num{width:66px;height:66px;border-radius:50%;background:var(--green);color:#fff;font-size:32px;font-weight:700;display:flex;align-items:center;justify-content:center}
.plan-card.active .num{background:#fff;color:var(--green)}
.plan-card h4{margin-top:28px;font-size:18.5px;font-weight:500;color:var(--ink);line-height:1.2}
.plan-card.active h4{color:#fff}
.plan-card ul{list-style:none;margin-top:14px;font-family:'Lato',sans-serif;font-size:12.5px;color:#333}
.plan-card.active ul{color:#fff}
.plan-card li{margin-bottom:12px}
.plan-card li::before{content:"›";color:var(--green);font-weight:700;margin-right:5px;font-size:15px}
.plan-card.active li::before{color:#fff}
.plan-card p{margin-top:12px;font-family:'Lato',sans-serif;font-size:12.5px;color:#333;line-height:1.45;padding-right:50px}
.plan-card svg{position:absolute;right:0;bottom:0}
.plan-cta{top:2770px}

/* crisis band */
.crisis-band{top:2855px;left:0;width:1200px;height:250px;background:linear-gradient(180deg,#2b2b2b,#3a3a3a)}
.crisis-pre{top:2920px;font-size:19px;color:#fff}
.crisis-title{top:2942px;font-size:42px;font-weight:800;color:#fff}
.crisis-cta{top:3004px}

/* footer */
.site-footer{top:3105px;left:0;width:1200px;height:336px;background:var(--footer-bg)}
.foot-head{top:3154px;font-size:18px;font-weight:500;color:var(--ink)}
.foot-list{list-style:none;font-family:'Lato',sans-serif;font-size:11px;color:#666}
.foot-list li{height:30px}
.foot-list li::before{content:"•";color:var(--green);margin-right:4px}
.phone{left:758px;top:3186px;font-family:'Lato',sans-serif;font-weight:700;font-size:14px;color:var(--ink)}
.foot-about{left:758px;top:3217px;width:340px;font-family:'Lato',sans-serif;font-size:11px;line-height:1.6;color:#666}
.site-footer-brand{left:758px;top:3284px}
.socials{top:3346px;left:576px;display:flex;gap:6px}
.socials span{width:20px;height:20px;border-radius:50%;background:#222}
.copyright{top:3375px;font-family:'Lato',sans-serif;font-size:11.5px;color:#333}
.copyright b{color:var(--green);font-weight:400}
</style>
</head>
<body>

<header class="abs site-header">
  <div class="brand"><span class="dot"></span>CrewBeacon</div>
  <nav class="nav">
    <a href="#">Home</a>
    <a href="#">Buy Addons</a>
    <a href="#" class="login">Cust Login</a>
    <a href="#" class="explore">Explore Your Choices</a>
  </nav>
</header>

<section class="abs hero" role="img" aria-label="Photo of a desk with a panic button mounted underneath"><div class="shade"></div></section>
<div class="abs slide-arrow prev"><svg width="10" height="12" viewBox="0 0 10 12"><path d="M7 1 2 6l5 5" fill="none" stroke="#fff" stroke-width="2"/></svg></div>
<div class="abs slide-arrow next"><svg width="10" height="12" viewBox="0 0 10 12"><path d="M3 1l5 5-5 5" fill="none" stroke="#fff" stroke-width="2"/></svg></div>
<div class="abs center hero-pre">FEEL CONFIDENT THAT</div>
<h1 class="abs center hero-title">YOUR STAFF IS <em>PROTECTED</em></h1>
<div class="abs center hero-sub">Get a Revolutionary New Electronic Panic Button</div>
<div class="abs center hero-cta"><a class="btn" href="#">Ready to get started</a></div>

<div class="abs feature-card blue" style="left:94px">
  <div class="photo" role="img" aria-label="Hand holding a wall-mounted alert device" style="background:linear-gradient(135deg,#8a8f93,#3f4246 60%,#c9cdd0)"></div>
  <div class="caption">Problems Stopped Before They Start For Any Type Of Organization</div>
</div>
<div class="abs feature-card green" style="left:436px">
  <div class="photo" role="img" aria-label="Several panic button units laid out on a table" style="background:linear-gradient(135deg,#e8d2b8,#c9a983 60%,#b8966f)"></div>
  <div class="caption">Affordable Prices Starting at $18 per month. No Contracts. No Hidden Costs.</div>
</div>
<div class="abs feature-card blue" style="left:776px">
  <div class="photo" role="img" aria-label="Alert device mounted on the side of a desk" style="background:linear-gradient(135deg,#9a8f85,#3a3836 55%,#d7d9db)"></div>
  <div class="caption">Alerts by computer, mobile device, text, phone, email, monitoring and E911</div>
</div>

<section class="abs alone-band"></section>
<div class="abs center alone-pre">YOUR EMPOYEES SHOULDNT</div>
<h2 class="abs center alone-title">FEEL ALONE WHEN THEY NEED HELP</h2>
<div class="abs center alone-sub">Does this problem make you feel frustrated and anxious? Put a simple solution in their hands !Ready</div>
<div class="abs center alone-cta"><a class="btn white" href="#">Ready to get started</a></div>

<div class="abs center why-pre">WHY</div>
<h2 class="abs center why-title">BUSINESSES CHOOSE US</h2>

<div class="abs reason" style="left:94px">
  <div class="icon" role="img" aria-label="Icon of a hand pressing a button"></div>
  <h3>EASY TO USE</h3>
  <p>Press a button and let the right people know you need help and open a chat window letting everyone talk on resolving their problem.</p>
</div>
<div class="abs reason" style="left:432px">
  <div class="icon" role="img" aria-label="Icon of a settings gear"></div>
  <h3>COMMUNICATE THE WAY YOU WANT</h3>
  <div class="lead">We give you lots of options:</div>
  <div class="options">
    <span>Computer</span><span>Text</span>
    <span>Mobile</span><span>E911</span>
    <span>Email</span><span>Call Center</span>
    <span>Phone call</span><span></span>
  </div>
</div>
<div class="abs reason" style="left:770px">
  <div class="icon" role="img" aria-label="Icon of a wall-mounted alert device"></div>
  <h3>COST EFFECTIVE PROTECTION</h3>
  <p>By leveraging your existing network and equipment we can lower your costs to give better options to your staff.</p>
</div>
<div class="abs center why-cta"><a class="btn" href="#">Ready to get started</a></div>

<div class="abs photo-phone" role="img" aria-label="Desk phone beside a panic button unit"></div>
<p class="abs split-text split-one">We know how scary it can feel to worry about employee safety.</p>
<div class="abs split-one-cta"><a class="btn" href="#">Start my demo</a></div>

<p class="abs split-text split-two">That's why we have provided a way for customers to get help to staff effectively in</p>
<div class="abs split-two-note">45 States <small>Covering</small> 5 Countries</div>
<div class="abs photo-lanyard" role="img" aria-label="Staff member wearing a panic button on a lanyard"></div>

<h2 class="abs center plan-title">SIMPLE START PLAN</h2>

<div class="abs plan-card" style="left:94px">
  <div class="num">1</div>
  <h4>Explore Your Choices</h4>
  <ul><li>Pricing</li><li>Trial</li><li>Quote</li><li>Hardware</li></ul>
  <svg width="200" height="140" viewBox="0 0 200 140"><path d="M200 0V140H0C110 125 190 90 200 0Z" fill="var(--blue)"/></svg>
</div>
<div class="abs plan-card active" style="left:437px">
  <div class="num">2</div>
  <h4>Get Setup</h4>
  <ul><li>Input Your Alerts</li><li>Input Your Staff</li><li>Install Our Software</li></ul>
  <svg width="200" height="140" viewBox="0 0 200 140"><path d="M200 0V140H0C110 125 190 90 200 0Z" fill="var(--green-dark)"/></svg>
</div>
<div class="abs plan-card" style="left:779px">
  <div class="num">3</div>
  <h4>Feel Confident Your Staff Is Protected</h4>
  <p>High Five. You just too a major step to getting rid of the anxiety and frustration this gave you.</p>
  <svg width="200" height="140" viewBox="0 0 200 140"><path d="M200 0V140H0C110 125 190 90 200 0Z" fill="var(--blue)"/></svg>
</div>
<div class="abs center plan-cta"><a class="btn" href="#">Start my demo</a></div>

<section class="abs crisis-band" role="img" aria-label="Dark photo of an office stairway"></section>
<div class="abs center crisis-pre">STAY CONNECTED WITH</div>
<h2 class="abs center crisis-title">STAFF DURING A CRISIS SITUATIONS</h2>
<div class="abs center crisis-cta"><a class="btn" href="#">Start my demo</a></div>

<footer class="abs site-footer"></footer>
<div class="abs foot-head" style="left:94px">SHOP</div>
<ul class="abs foot-list" style="left:94px;top:3186px"><li>Add Ons</li><li>Start My Demo</li><li>Custom Quote</li><li>Start Trial</li></ul>
<div class="abs foot-head" style="left:282px">LEGAL</div>
<ul class="abs foot-list" style="left:282px;top:3186px"><li>Privacy Policy</li><li>Terms of Use</li><li>End User License</li><li>Agreement</li></ul>
<div class="abs foot-head" style="left:473px">ABOUT</div>
<ul class="abs foot-list" style="left:473px;top:3186px"><li>Affiliates</li><li>Contact</li><li>Support</li><li>Existing Customer</li></ul>
<ul class="abs foot-list" style="left:600px;top:3186px"><li>Industries</li><li>Blog</li><li>FAQ</li></ul>
<div class="abs foot-head" style="left:758px">CALL US</div>
<div class="abs phone">1 – 800 – 555 – 0147</div>
<p class="abs foot-about">When employees feel alone during a threatening situation, we give them a way to let the right resources know that they need help so you can feel confident that your staff is protected.</p>
<div class="abs brand site-footer-brand"><span class="dot"></span>CrewBeacon</div>
<div class="abs socials"><span></span><span></span></div>
<div class="abs center copyright">COPYRIGHT © 2020 <b>CREWBEACON</b>. ALL RIGHTS RESERVED.</div>

</body>
</html>
```